TKA Electricial Contracting Services

Hi guys, after a design for my small electrical company, have logo design files to be incorporated into the layout, the basic concept is electrical contracting services for residential, commercial, industrial & data services, image is clean clear and strong,

Card format is to have a nice clean logo on front,with maybe the Residential – commercial – industrial - data, followed with licensed & insured, followed by contact details on backside of the card.

Target Market(s)

Residential, commercial, industrial sectors.

Industry/Entity Type

Electrical

Contact Information for Business Card

TKA logo,
Residential – commercial – industrial - data
REC: 61372
Email: tka@poralink.net.au
Phone: 0458 203 719

Requirements
Must have
• Clean & strong design.
Nice to have
• If possible, I would like the logo colours inverted so the text is orange and the background is black on the front of the card, then the backside of the card be the reverse colour
Should not have
• No Sparks, lightning bolts,

```html
<!DOCTYPE html>
<html lang="en">
<head>
<meta charset="utf-8">
<title>TKA Electrical – Business Card</title>
<link rel="stylesheet" href="https://fonts.googleapis.com/css2?family=Lato:wght@400;700;900&display=swap">
<style>
  :root {
    --backdrop: #202020;
    --card-black: #050505;
    --orange: #f07f1e;
    --orange-deep: #e0711a;
    --ink-dark: #1a1a1a;
    --text-light: #e6e6e6;
    --bullet-grey: #8a8a8a;
  }
  * { margin: 0; padding: 0; box-sizing: border-box; }
  html, body { width: 1200px; height: 873px; overflow: hidden; }
  body {
    background: var(--backdrop);
    font-family: "Lato", sans-serif;
    position: relative;
  }
  .card {
    position: absolute;
    background: var(--card-black);
    border-radius: 18px;
    overflow: hidden;
    box-shadow: 0 10px 30px rgba(0,0,0,.55);
  }

  /* Front card */
  .card-front {
    left: 70px; top: 290px;
    width: 540px; height: 310px;
  }
  .front-brand {
    position: absolute; left: 0; right: 0; top: 70px;
    text-align: center; color: var(--orange); font-weight: 900;
  }
  .front-brand .brand-mark { font-size: 78px; line-height: 1; letter-spacing: 2px; }
  .front-brand .brand-name { font-size: 17px; letter-spacing: .5px; margin-top: 2px; }
  .services {
    position: absolute; left: 0; right: 0; bottom: 46px;
    text-align: center; color: var(--orange); font-weight: 700;
    font-size: 15px; line-height: 1.55;
  }
  .services .dot { color: var(--bullet-grey); margin: 0 5px; }

  /* Back card */
  .card-back {
    left: 700px; top: 140px;
    width: 360px; height: 600px;
  }
  .back-brand {
    position: absolute; left: 0; right: 0; top: 58px;
    text-align: center; color: var(--orange); font-weight: 900;
  }
  .back-brand .brand-mark { font-size: 64px; line-height: 1; letter-spacing: 2px; }
  .back-brand .brand-name { font-size: 14px; margin-top: 2px; }
  .name-band {
    position: absolute; left: 0; right: 0; top: 200px; height: 96px;
    background: var(--orange);
    text-align: center; padding-top: 22px;
  }
  .person-name { color: var(--ink-dark); font-weight: 900; font-size: 28px; }
  .person-role { color: #fff; font-weight: 700; font-size: 15px; letter-spacing: 1px; margin-top: 2px; }
  .contact-icons {
    position: absolute; left: 0; right: 0; top: 318px;
    display: flex; justify-content: center; gap: 24px;
  }
  .contact-icons svg { width: 22px; height: 22px; fill: var(--orange); }
  .contact-list {
    position: absolute; left: 0; right: 0; top: 358px;
    text-align: center; color: var(--text-light); font-size: 18px; line-height: 1.35;
  }
  .contact-list p { margin-bottom: 10px; white-space: nowrap; }
  .credentials-band {
    position: absolute; left: 0; right: 0; bottom: 0; height: 118px;
    background: var(--orange-deep);
    text-align: center; color: var(--ink-dark); padding-top: 20px;
    font-size: 16px; font-weight: 700; letter-spacing: .5px; line-height: 1.5;
  }
  .credentials-band div { white-space: nowrap; }
</style>
</head>
<body>

  <section class="card card-front" aria-label="Card front">
    <div class="front-brand">
      <div class="brand-mark">TKA</div>
      <div class="brand-name">Tarek Kane Electrical</div>
    </div>
    <div class="services">
      <div><span class="dot">•</span>New installations<span class="dot">•</span>Additions<span class="dot">•</span>Lighting<span class="dot">•</span>Repairs<span class="dot">•</span></div>
      <div><span class="dot">•</span>Maintenance 24 hours<span class="dot">•</span>Assistance<span class="dot">•</span></div>
    </div>
  </section>

  <section class="card card-back" aria-label="Card back">
    <div class="back-brand">
      <div class="brand-mark">TKA</div>
      <div class="brand-name">Tarek Kane Electrical</div>
    </div>

    <div class="name-band">
      <div class="person-name">Marcus Hale</div>
      <div class="person-role">INCHARGE</div>
    </div>

    <div class="contact-icons">
      <svg viewBox="0 0 24 24" aria-label="Phone"><path d="M6.6 10.8a15.1 15.1 0 0 0 6.6 6.6l2.2-2.2c.3-.3.7-.4 1-.2 1.1.4 2.3.6 3.6.6.6 0 1 .4 1 1V20c0 .6-.4 1-1 1A17 17 0 0 1 3 4c0-.6.4-1 1-1h3.5c.6 0 1 .4 1 1 0 1.3.2 2.5.6 3.6.1.3 0 .7-.2 1z"/></svg>
      <svg viewBox="0 0 24 24" aria-label="Email"><path d="M2 5h20v14H2zM3.5 6.5 12 13l8.5-6.5v-.1h-17z" fill-rule="evenodd"/></svg>
    </div>

    <div class="contact-list">
      <p>0458 203 719</p>
      <p>tka@poralink.net.au</p>
      <p>REC: 61372</p>
    </div>

    <div class="credentials-band">
      <div>LICENCED &amp; INSURED</div>
      <div>RESIDENTIAL – COMMERCIAL</div>
      <div>INDUSTRIAL – DATA</div>
    </div>
  </section>

</body>
</html>
```